Trifold brochure for new business - KiteNest Parenting

I need a trifold brochure that outlines who we are, the services we provide, our price list and contact details.

I would like a clean, bold modern design. I have some photos and logos that I am licensed to use for the services I provide.

I do not want anything cute or feminine as I need it to appeal to men, women and other business professionals including doctors and hospitals.

I have a logo and the content will be taken from my website - www.kitenestparenting.example.

Target Market(s)

Expecting parents, parents of newborns, parents of toddlers

Industry/Entity Type

Business

Font styles to use
Sans Serif

Requirements
Must have
• Emphasis on who we are and what we believe. A clear outline of our services. A clear price list. A map of our location and contact details. I would like it to fit the style of the KiteNest Parenting logo.

```html
<!DOCTYPE html>
<html lang="en">
<head>
<meta charset="utf-8">
<title>KiteNest Parenting – Trifold Brochure</title>
<link rel="stylesheet" href="https://fonts.googleapis.com/css2?family=Open+Sans:ital,wght@0,400;0,600;0,700;0,800;1,400&family=Roboto+Slab:wght@300;400&family=Archivo+Black&display=swap">
<style>
:root{
  --green:#3fae49;
  --green-deep:#2e9a5a;
  --charcoal:#58595b;
  --ink:#3a3a3c;
  --paper:#f4f4f4;
  --paper-edge:#e4e4e4;
  --stage:#c9c9c9;
  --white:#ffffff;
}
*{box-sizing:border-box;margin:0;padding:0}
html,body{width:1200px;height:880px;overflow:hidden}
body{
  background:radial-gradient(ellipse at center,#dcdcdc 0%,var(--stage) 75%);
  font-family:"Open Sans",Arial,sans-serif;
  color:var(--ink);
  position:relative;
}
.brochure{
  position:absolute;left:90px;top:45px;
  width:1020px;height:790px;
  display:flex;
  box-shadow:0 10px 30px rgba(0,0,0,.25);
}
.panel{position:relative;width:340px;height:790px;overflow:hidden}
.panel + .panel{border-left:1px solid var(--paper-edge)}

/* ---------- price panel ---------- */
.panel--prices{background:var(--green);color:var(--white);padding:86px 26px 0 26px}
.price-badge{
  position:absolute;right:22px;top:22px;width:66px;height:66px;border-radius:50%;
  background:var(--charcoal);color:var(--white);
  display:flex;align-items:center;justify-content:center;text-align:center;
  font-weight:700;font-size:14px;line-height:1.05;
}
.price-group{margin-bottom:14px}
.price-group h3{font-size:12.5px;font-weight:700;margin-bottom:3px}
.price-group p{font-size:11px;line-height:1.4}
.price-list{list-style:none;font-size:11px;line-height:1.4}
.price-list li{padding-left:11px;position:relative}
.price-list li::before{content:"•";position:absolute;left:0}
.packages{
  position:absolute;left:0;right:0;top:448px;height:220px;
  background:var(--charcoal);padding:20px 26px;
}
.packages h2{font-size:15px;font-weight:700;text-align:center;margin-bottom:10px}
.packages h3{font-size:12px;font-weight:700}
.packages .price-list{margin-bottom:10px;font-size:10.5px}

/* ---------- contact panel ---------- */
.panel--contact{background:linear-gradient(180deg,var(--white) 0%,var(--paper) 100%)}
.quote{
  position:absolute;left:65px;top:30px;width:210px;height:210px;border-radius:50%;
  background:var(--green-deep);color:var(--white);
  display:flex;flex-direction:column;align-items:center;justify-content:center;text-align:center;
}
.quote blockquote{font-family:"Roboto Slab",Georgia,serif;font-weight:300;font-size:17px;line-height:1.25}
.quote cite{font-style:normal;font-size:10px;margin-top:8px;padding-top:5px;border-top:1px solid rgba(255,255,255,.7)}
.brand{display:flex;align-items:center;gap:9px}
.brand__mark{width:34px;height:34px;border-radius:50%;background:var(--green);flex:none}
.brand__name{font-weight:700;font-size:21px;color:var(--green);white-space:nowrap}
.brand__tag{font-size:11.5px;color:var(--charcoal);font-style:italic;margin-top:3px}
.panel--contact .brand-block{position:absolute;left:52px;top:290px}
.contact-swoosh{position:absolute;left:0;top:330px;width:340px;height:70px}
.owner{position:absolute;left:0;right:0;top:392px;text-align:center;font-weight:700;font-size:12.5px}
.contact-list{position:absolute;left:40px;top:430px;list-style:none;font-size:13px;font-weight:700}
.contact-list li{display:flex;align-items:center;gap:9px;margin-bottom:7px}
.contact-list svg{width:15px;height:15px;flex:none}
.follow{position:absolute;left:40px;top:530px}
.follow h4{color:var(--green);font-size:13px;font-weight:700;margin-bottom:6px}
.social{display:grid;grid-template-columns:150px 120px;row-gap:8px;list-style:none;font-size:12px;font-weight:700}
.social li{display:flex;align-items:center;gap:7px}
.social .dot{width:15px;height:15px;border-radius:50%;background:var(--charcoal);flex:none}
.social .dot--green{background:var(--green)}
.contact-rule{position:absolute;left:0;top:600px;width:340px;height:60px}

/* ---------- cover panel ---------- */
.panel--cover{background:linear-gradient(180deg,var(--paper) 0%,var(--white) 100%)}
.panel--cover .brand-block{position:absolute;left:34px;top:52px}
.panel--cover .brand__mark{width:44px;height:44px}
.panel--cover .brand__name{font-size:25px}
.panel--cover .brand__tag{font-size:13px}
.cover-gallery{position:absolute;left:0;top:130px;width:340px;height:500px}
.cover-url{
  position:absolute;left:0;right:0;top:672px;text-align:center;
  font-family:"Archivo Black","Arial Black",sans-serif;font-size:25px;letter-spacing:-.3px;
}
.cover-url .url-brand{color:var(--green)}
.cover-url .url-rest{color:var(--charcoal)}
.cover-url .url-tld{color:var(--charcoal);font-size:17px}
</style>
</head>
<body>
<main class="brochure">

  <!-- Price list panel -->
  <section class="panel panel--prices">
    <div class="price-badge">Price<br>List</div>

    <div class="price-group">
      <h3>CradleEase™ Workshops and Courses:</h3>
      <ul class="price-list">
        <li>CradleEase™ Pre-Natal or Newborn Workshop - $75 per person or couple</li>
        <li>CradleEase™ 4-Week Mother and Baby Course - $200 per person or couple</li>
        <li>CradleEase™ Baby Led Weaning Workshop - $50 per person or couple</li>
      </ul>
    </div>

    <div class="price-group">
      <h3>TotSteady™ Workshops and Courses:</h3>
      <ul class="price-list">
        <li>TotSteady™ 4-Week Parenting Course - $200 per person or couple</li>
        <li>TotSteady™ Toddler Calming Workshop - $75 per person or couple</li>
      </ul>
    </div>

    <div class="price-group">
      <h3>Private Workshops and Courses:</h3>
      <p>Any of the above workshops and courses can be offered privately</p>
      <ul class="price-list">
        <li>Private 4-week courses - $350 per person or couple</li>
        <li>Private 3-hour workshops - $125 per person or couple</li>
      </ul>
    </div>

    <div class="packages">
      <h2>Packages and Discounts</h2>
      <h3>Prepared for Parenthood Package: $300 (value $325)</h3>
      <ul class="price-list">
        <li>CradleEase™ Calming Workshop (pre-birth or newborn)</li>
        <li>CradleEase™ 4-Week Mother and Baby Course</li>
        <li>CradleEase™ Baby Led Weaning Workshop</li>
      </ul>
      <h3>Parenting Toddlers Package: $250 (value $275)</h3>
      <ul class="price-list">
        <li>TotSteady™ Toddler Calming Workshop</li>
        <li>TotSteady™ 4-week Parenting Course</li>
      </ul>
    </div>
  </section>

  <!-- Contact panel -->
  <section class="panel panel--contact">
    <figure class="quote">
      <blockquote>I did then what I<br>knew how to do.<br>Now I know better,<br>I do better.</blockquote>
      <cite>Mara Ellison</cite>
    </figure>

    <div class="brand-block">
      <div class="brand">
        <span class="brand__mark"></span>
        <span class="brand__name">KiteNest Parenting</span>
      </div>
      <p class="brand__tag">Empowering parents through knowledge</p>
    </div>

    <svg class="contact-swoosh" viewBox="0 0 340 70" aria-hidden="true">
      <path d="M0 8 Q170 70 340 52" fill="none" stroke="#58595b" stroke-width="5"/>
    </svg>

    <p class="owner">Renee Hollis-Ward - Founder/ Owner</p>

    <ul class="contact-list">
      <li>
        <svg viewBox="0 0 16 16" aria-hidden="true"><path d="M8 1a5 5 0 0 0-5 5c0 4 5 9 5 9s5-5 5-9a5 5 0 0 0-5-5zm0 7a2 2 0 1 1 0-4 2 2 0 0 1 0 4z" fill="#3fae49"/></svg>
        18 Alderbrook Lane, Marlow, TX
      </li>
      <li>
        <svg viewBox="0 0 16 16" aria-hidden="true"><path d="M4 1l2.5 3-1.5 2a9 9 0 0 0 5 5l2-1.5 3 2.5-1.5 2.5C8 14 2 8 1.5 2.5z" fill="#3fae49"/></svg>
        555.014.2761
      </li>
      <li>
        <svg viewBox="0 0 16 16" aria-hidden="true"><rect x="1" y="3" width="14" height="10" fill="#3fae49"/><path d="M1 3l7 6 7-6" fill="none" stroke="#fff" stroke-width="1.3"/></svg>
        renee@kitenestparenting.example
      </li>
    </ul>

    <div class="follow">
      <h4>Follow us</h4>
      <ul class="social">
        <li><span class="dot"></span>reneecradleease</li>
        <li><span class="dot"></span>rhollisward</li>
        <li><span class="dot dot--green"></span>knparenting</li>
      </ul>
    </div>

    <svg class="contact-rule" viewBox="0 0 340 60" aria-hidden="true">
      <path d="M0 4 Q170 60 340 40" fill="none" stroke="#3fae49" stroke-width="4"/>
    </svg>
  </section>

  <!-- Cover panel -->
  <section class="panel panel--cover">
    <div class="brand-block">
      <div class="brand">
        <span class="brand__mark"></span>
        <span class="brand__name">KiteNest Parenting</span>
      </div>
      <p class="brand__tag">Empowering parents through knowledge</p>
    </div>

    <svg class="cover-gallery" viewBox="0 0 340 500" role="img" aria-label="Photo collage of newborn babies and a smiling toddler in dungarees surrounded by colourful painted handprints">
      <defs>
        <linearGradient id="gallery-tone" x1="0" y1="0" x2="1" y2="1">
          <stop offset="0" stop-color="#e9d3c4"/>
          <stop offset=".45" stop-color="#f3efe9"/>
          <stop offset=".7" stop-color="#b9cfe0"/>
          <stop offset="1" stop-color="#d9c2b2"/>
        </linearGradient>
      </defs>
      <path d="M0 30 Q170 -10 340 40 L340 470 Q170 520 0 420 Z" fill="url(#gallery-tone)"/>
      <path d="M0 30 Q170 -10 340 40" fill="none" stroke="#3fae49" stroke-width="4"/>
      <path d="M0 420 Q170 520 340 470" fill="none" stroke="#3fae49" stroke-width="4"/>
      <path d="M0 150 Q170 100 340 170" fill="none" stroke="#ffffff" stroke-width="3"/>
      <path d="M0 330 Q170 400 340 360" fill="none" stroke="#ffffff" stroke-width="3"/>
    </svg>

    <p class="cover-url"><span class="url-brand">KiteNest</span><span class="url-rest">Parenting</span><span class="url-tld">.example</span></p>
  </section>

</main>
</body>
</html>
```